Zentrival IT Company Business Card

📌 Objective:
Create a modern, fluid and stylish business card that reflects the identity of our IT company and our partnership with Quandora.
📍 Key information:
• Company name: Zentrival
• Activity: Quandora 520 Expert
• Colors to favor: Inspired by the Zentrival logo
• Style: Minimalist, modern, professional
• Front / Back:
• Items to include:
o Company logo
o Name and surname
o Post
o Email
o Phone
o Website
o QR code (optional)
🎨 Inspirations & Expectations:
• Sleek design with a high-tech touch
• Possibly subtle graphic elements linked to the Quandora universe
• Good readability and balance between text and visuals

Lent pour commenter

Target Market(s)

Private, public

Contact Information for Business Card

Quandora520, Formation, Gouvernance, Migration, Sécurité

Colors
6B429C
8869AF
B7A5CE
E3DAEB
F3F0F8

Requirements
Nice to have
• Have the icons of the applications I work on

```html
<!DOCTYPE html>
<html lang="en">
<head>
<meta charset="utf-8">
<title>Zentrival Business Card</title>
<link href="https://fonts.googleapis.com/css2?family=Montserrat:wght@400;500;700;800&display=swap" rel="stylesheet">
<style>
  :root{
    --bg:#3a3b3d;
    --card-white:#ffffff;
    --card-black:#1b1b1b;
    --ink:#111111;
    --ink-soft:#222222;
    --cyan:#17a9cc;
    --blue:#2f7fe0;
    --purple:#b43cf6;
    --edge-blue:#1f7fd0;
    --label-bg:#f3f0f8;
    --label-ink:#6b429c;
  }
  *{box-sizing:border-box;margin:0;padding:0}
  html,body{width:1200px;height:1200px;overflow:hidden}
  body{
    background:var(--bg);
    font-family:"Montserrat",Arial,sans-serif;
    display:flex;flex-direction:column;align-items:center;justify-content:center;gap:60px;
  }
  .card{
    width:880px;height:503px;border-radius:34px;position:relative;overflow:hidden;
    box-shadow:0 18px 40px rgba(0,0,0,.45);
  }
  .card--front{background:var(--card-white)}
  .card--front .accent-band{
    position:absolute;left:0;right:0;bottom:0;height:16px;
    background:linear-gradient(90deg,var(--cyan) 0%,var(--blue) 55%,var(--purple) 100%);
  }
  .contact{
    position:absolute;left:70px;top:205px;
  }
  .contact__name{
    color:var(--cyan);font-weight:700;font-size:40px;letter-spacing:.5px;line-height:1;
  }
  .contact__title{
    color:var(--ink-soft);font-weight:500;font-size:30px;margin:4px 0 22px;line-height:1;
  }
  .contact__list{list-style:none}
  .contact__item{
    display:flex;align-items:flex-start;gap:14px;font-size:21px;color:var(--ink);
    line-height:1.2;margin-bottom:10px;
  }
  .contact__icon{width:24px;height:24px;flex:none;margin-top:1px}
  .brand{
    position:absolute;right:70px;top:130px;display:flex;flex-direction:column;align-items:center;
  }
  .wordmark{
    display:flex;align-items:center;gap:14px;
  }
  .wordmark__dot{width:26px;height:26px;border-radius:50%;background:var(--purple)}
  .wordmark__text{font-weight:700;font-size:62px;letter-spacing:-1px;line-height:1}
  .card--front .wordmark__text{color:var(--ink)}
  .apps{
    display:flex;gap:8px;margin-top:34px;
  }
  .apps__item{
    background:var(--label-bg);color:var(--label-ink);font-weight:500;font-size:14px;
    padding:7px 10px;border-radius:8px;
  }
  .card--back{
    background:var(--card-black);
    border-bottom:4px solid var(--edge-blue);
    display:flex;align-items:center;justify-content:center;
  }
  .card--back .wordmark__text{color:#ffffff;font-size:104px}
  .card--back .wordmark__dot{width:40px;height:40px}
</style>
</head>
<body>
  <section class="card card--front" aria-label="Business card front">
    <div class="contact">
      <p class="contact__name">FULL NAME</p>
      <p class="contact__title">TITLE</p>
      <ul class="contact__list">
        <li class="contact__item">
          <svg class="contact__icon" viewBox="0 0 24 24" aria-hidden="true"><path fill="var(--cyan)" d="M6.6 10.8a15 15 0 0 0 6.6 6.6l2.2-2.2c.3-.3.7-.4 1-.2 1.1.4 2.3.6 3.6.6.6 0 1 .4 1 1V20c0 .6-.4 1-1 1A17 17 0 0 1 3 4c0-.6.4-1 1-1h3.5c.6 0 1 .4 1 1 0 1.3.2 2.5.6 3.6.1.3 0 .7-.2 1z"/></svg>
          <span>(000) 000 0000</span>
        </li>
        <li class="contact__item">
          <svg class="contact__icon" viewBox="0 0 24 24" aria-hidden="true"><rect x="2" y="5" width="20" height="14" rx="1.5" fill="var(--cyan)"/><path d="M3 6l9 7 9-7" fill="none" stroke="#fff" stroke-width="1.6"/></svg>
          <span>email@company.com</span>
        </li>
        <li class="contact__item">
          <svg class="contact__icon" viewBox="0 0 24 24" aria-hidden="true"><g fill="none" stroke="var(--cyan)" stroke-width="1.8"><circle cx="12" cy="12" r="9.5"/><ellipse cx="12" cy="12" rx="4" ry="9.5"/><path d="M2.5 12h19M4 7h16M4 17h16"/></g></svg>
          <span>www.company.com</span>
        </li>
        <li class="contact__item">
          <svg class="contact__icon" viewBox="0 0 24 24" aria-hidden="true"><path fill="var(--cyan)" d="M12 2a7 7 0 0 0-7 7c0 5 7 13 7 13s7-8 7-13a7 7 0 0 0-7-7zm0 9.5A2.5 2.5 0 1 1 12 6.5a2.5 2.5 0 0 1 0 5z"/></svg>
          <span>123 Name Street, 000<br>Your City, 00000-000</span>
        </li>
      </ul>
    </div>

    <div class="brand">
      <div class="wordmark">
        <span class="wordmark__dot" aria-hidden="true"></span>
        <span class="wordmark__text">Zentrival</span>
      </div>
      <ul class="apps" style="list-style:none">
        <li class="apps__item">Mailory</li>
        <li class="apps__item">Flowset</li>
        <li class="apps__item">Pilotra</li>
        <li class="apps__item">Sharelon</li>
        <li class="apps__item">Groupvine</li>
      </ul>
    </div>

    <div class="accent-band" aria-hidden="true"></div>
  </section>

  <section class="card card--back" aria-label="Business card back">
    <div class="wordmark">
      <span class="wordmark__dot" aria-hidden="true"></span>
      <span class="wordmark__text">Zentrival</span>
    </div>
  </section>
</body>
</html>
```